Amazing Homepage required for Ireland's Top Crowdfunding site

Design/ PSD Files required.

BrookLedger.com is the market leader in crowd lending/peer to peer lending in Ireland. Businesses/SME’s can borrow anything from €5,000 to €100,000 at interest rates much more favourable than those offered by the banks. BL is also a quicker and less bureaucratic than traditional lending institutions. We are a viable alternative to banks and traditional sources of finance.

Our lenders are members of the public and they can lend directly to Irish businesses in amounts from €50 to €2,000. They get a better rate of return than deposit accounts, as well as the feel good factor of supporting a local business.

We have just completed a full rebrand of our logo and colours and would now like to utilise these to best effect by implementing them in a total redesign of our homepage to attract borrowers and lenders. Please see the attached files for the brand guidelines and logo/colours to be used.

We are looking for a designer to utilise our new branding in a creative way, conveying that we are modern, trustworthy, competitive and friendly/local.

We currently have two different user groups:
1- Lenders; this currently consists of members of the public but in future will expand to include financial institutions

2- Business borrowers looking for funds for their business

Embracing and balancing both of these user groups is difficult so we would like the homepage to primarily target borrowers but incorporate clear alternative calls to action for lenders/prospective lenders as well.

We would like:
Infinite scroll homepage
New logo and tagline on a fixed header which should also include; ‘Marketplace’ ‘About’ ‘FAQ’ and a clear login button
A static full bleed image
Overlaid over this we would like a loan calculator in a similar style/functionality to this one on www.pelvaro.com. It should have:
an image of a slider icon with amounts from €0 to €100,000
A text field with ‘Business Loan amount’ which fills when the slider is moved
Then, a text field called ‘Monthly repayment’
An email field with a clear call to action ie ‘Go’ or ‘Get Started’
The purpose of this is to enable prospective borrowers to quickly and easily get a quote estimate for their loan
Underneath this we would like to have an alternate call to action to target prospective lenders; something like ‘Looking to Lend?’

Further down the page we would like to have a heading ‘What is Brook Ledger?’
(include information from company overview)

3 images to illustrate loans live in our Marketplace

Target Market(s)

This Homepge should appeal to small business owners

Industry/Entity Type

Crowd

Number of Pages Required

1 page

Font styles to use
Sans Serif

Requirements
Must have
• Linear clean and modern homepage
• Clear calls to action
Nice to have
• Ideas for how video/rich media might be incorporated into a future iteration of the homepage

```html
<!DOCTYPE html>
<html lang="en">
<head>
<meta charset="utf-8">
<title>Brook Ledger – Business Crowdfunding</title>
<link href="https://fonts.googleapis.com/css2?family=Open+Sans:wght@400;600;700&display=swap" rel="stylesheet">
<style>
:root{
  --orange:#f0531f;
  --orange-dark:#d8421a;
  --ink:#333333;
  --muted:#777777;
  --paper:#f3f3f1;
  --dark:#262626;
  --darker:#1c1c1c;
  --white:#ffffff;
}
*{box-sizing:border-box;margin:0;padding:0}
html,body{width:1200px;height:3708px;overflow:hidden}
body{font-family:'Open Sans',Arial,sans-serif;color:var(--ink);background:var(--white);position:relative}
.abs{position:absolute}

/* header */
.site-header{position:absolute;left:0;top:0;width:1200px;height:92px;background:rgba(20,16,12,.72);z-index:5}
.brand{position:absolute;left:44px;top:18px;color:var(--white)}
.brand-name{font-size:30px;font-weight:700;line-height:34px}
.brand-tag{font-size:13px;color:#ddd;margin-top:2px}
.account-links{position:absolute;right:44px;top:8px;display:flex;gap:10px;font-size:12px}
.account-links .login{background:var(--orange);color:#fff;padding:3px 12px;font-weight:700}
.account-links .create{color:#fff;padding:3px 6px}
.main-nav{position:absolute;right:44px;top:46px;display:flex;gap:6px;font-size:19px;color:#fff}
.main-nav span{padding:4px 14px}
.main-nav .active{background:var(--orange)}

/* hero */
.hero{position:absolute;left:0;top:0;width:1200px;height:960px;background:linear-gradient(180deg,#3c2d22 0%,#6b4e38 35%,#4a3628 70%,#2c2019 100%)}
.hero-title{position:absolute;top:318px;width:1200px;text-align:center;color:#fff;font-size:52px;font-weight:700}
.hero-sub{position:absolute;top:390px;width:1200px;text-align:center;color:#fff;font-size:34px}
.quote-panel{position:absolute;left:216px;top:522px;width:448px;height:410px;background:rgba(25,20,16,.82);padding:24px 24px}
.quote-panel p{color:#fff;font-size:15px;margin:0 0 16px 8px}
.field{height:40px;margin:0 80px 12px 8px;background:#8a8480;color:#eee;font-size:15px;line-height:40px;padding-left:14px}
.btn{display:inline-block;background:var(--orange);color:#fff;font-weight:600;text-align:center}
.quote-panel .btn{position:absolute;right:40px;bottom:30px;width:140px;height:42px;line-height:42px;font-size:17px}
.rate-tab{position:absolute;left:660px;top:530px;background:var(--orange);color:#fff;font-weight:700;font-size:17px;padding:6px 20px}
.rate-panel{position:absolute;left:664px;top:566px;width:316px;height:376px;background:var(--orange);padding:18px 22px;color:#fff}
.rate-row{display:flex;justify-content:space-between;align-items:center;font-size:15px}
.rate-input{background:#fff;color:var(--ink);width:100px;height:32px;line-height:32px;padding-left:10px;font-weight:600}
.slider{position:relative;height:4px;background:rgba(255,255,255,.55);margin:22px 0 34px}
.slider i{position:absolute;top:-8px;width:14px;height:20px;background:#fff;border-radius:3px}
.slider .lbl{position:absolute;top:12px;font-size:11px}
.rate-summary{display:flex;justify-content:space-between;font-size:12px;line-height:16px;margin-top:10px}
.rate-summary b{font-size:14px;display:block}
.rate-panel .btn{position:absolute;left:70px;bottom:22px;width:176px;height:44px;line-height:44px;background:var(--orange-dark);font-size:16px;border:1px solid rgba(255,255,255,.5)}

/* about */
.about{position:absolute;left:0;top:960px;width:1200px;height:768px;background:var(--paper)}
.section-title{text-align:center;font-size:38px;font-weight:600;color:var(--ink)}
.divider{display:flex;justify-content:center;align-items:center;gap:14px;margin:14px 0}
.divider span{width:60px;height:1px;background:#bbb}
.divider i{width:12px;height:12px;background:var(--orange);transform:rotate(45deg)}
.about .lead{text-align:center;font-size:15px;color:var(--muted)}
.about .intro{width:760px;margin:36px auto 0;text-align:center;font-size:16px;line-height:26px;color:#555}
.feature{position:absolute;width:300px;text-align:center}
.diamond{width:62px;height:62px;margin:0 auto;background:var(--orange);transform:rotate(45deg);display:flex;align-items:center;justify-content:center}
.diamond svg{transform:rotate(-45deg)}
.feature h3{font-size:19px;font-weight:600;margin:30px 0 14px}
.feature p{font-size:14px;line-height:22px;color:#666}
.about .btn{position:absolute;left:510px;top:598px;width:180px;height:44px;line-height:44px;font-size:16px}

/* how it works */
.how{position:absolute;left:0;top:1728px;width:1200px;height:536px;background:linear-gradient(90deg,#2a221c 0%,#4b3a2e 45%,#3a2d24 75%,#2b241f 100%)}
.how .section-title{color:#fff;font-weight:400;position:absolute;left:0;width:860px;top:34px}
.how .intro{position:absolute;left:210px;top:110px;width:440px;text-align:center;color:#eee;font-size:15px;line-height:23px}
.step{position:absolute;top:238px;width:210px;text-align:center;color:#fff}
.step-pic{width:110px;height:110px;margin:14px auto 0;transform:rotate(45deg);border:3px solid #c9a27a;background:linear-gradient(135deg,#7a5a44,#3a2a20)}
.step h4{margin-top:34px;font-size:15px;font-weight:700}
.step p{font-size:13px;line-height:19px;color:#ddd;margin-top:6px}
.person{position:absolute;left:860px;top:56px;width:262px;height:480px;background:linear-gradient(180deg,#8a6a55 0%,#c9b7ab 40%,#f2f0ee 70%,#2f3c6b 100%)}

/* lend band */
.lend{position:absolute;left:0;top:2264px;width:1200px;height:376px;background:var(--orange);color:#fff;text-align:center}
.lend h2{font-size:40px;font-weight:700;margin-top:40px}
.lend .sub{font-size:18px;margin-top:6px}
.lend .intro{width:820px;margin:30px auto 0;font-size:16px;line-height:25px}
.lend .btn{margin-top:26px;width:194px;height:46px;line-height:46px;background:var(--orange-dark);border:1px solid rgba(255,255,255,.5);font-size:16px}
.watch{margin-top:14px;font-size:14px;display:flex;justify-content:center;align-items:center;gap:8px}

/* gigs */
.gigs{position:absolute;left:0;top:2640px;width:1200px;height:356px;background:#fff}
.gigs .section-title{margin-top:40px;font-size:36px}
.gigs .lead{text-align:center;font-size:17px;color:var(--muted);margin-top:8px}
.video{position:absolute;top:212px;width:244px;height:142px;display:flex;align-items:center;justify-content:center}
.play{width:52px;height:36px;border-radius:8px;background:rgba(0,0,0,.7);display:flex;align-items:center;justify-content:center}

/* testimonials */
.testimonials{position:absolute;left:0;top:2996px;width:1200px;height:268px;background:var(--paper)}
.quote-box{position:absolute;left:22px;top:24px;width:1156px;height:218px;background:#fff;border:1px solid #ddd}
.quote{position:absolute;top:50px;width:460px;display:flex;gap:28px;align-items:center}
.badge{width:90px;height:90px;border-radius:50%;background:#e4e4e4;flex:none}
.quote p{font-size:14px;line-height:22px;color:#555}
.see-more{position:absolute;right:24px;bottom:14px;font-size:11px;color:#888}

/* footer */
.site-footer{position:absolute;left:0;top:3264px;width:1200px;height:444px;background:var(--dark);color:#ccc}
.footer-brand{position:absolute;left:54px;top:130px;color:#fff}
.footer-brand .brand-name{font-size:28px}
.social{position:absolute;left:54px;top:210px;display:flex;gap:14px}
.social i{width:22px;height:22px;background:#9a9a9a;display:block}
.fcol{position:absolute;top:50px;font-size:15px;line-height:26px}
.fcol h5{font-size:17px;font-weight:600;color:#fff;margin-bottom:8px}
.fcol li{list-style:none;padding-left:14px;position:relative}
.fcol li:before{content:"";position:absolute;left:0;top:11px;width:5px;height:5px;background:#888}
.seal{width:110px;height:34px;background:#cfd3d8;margin-top:10px}
.copyright{position:absolute;left:0;bottom:0;width:1200px;height:56px;background:var(--darker);font-size:13px;color:#888;line-height:56px;padding-left:54px}
</style>
</head>
<body>

<div class="hero" role="img" aria-label="Business owner standing in his café"></div>

<header class="site-header">
  <div class="brand"><div class="brand-name">Brook Ledger</div><div class="brand-tag">the business lending people</div></div>
  <div class="account-links"><span class="login">LOGIN</span><span class="create">Create Account</span></div>
  <nav class="main-nav"><span class="active">Marketplace</span><span>Lend</span><span>Borrow</span><span>About</span><span>FAQ</span></nav>
</header>

<h1 class="hero-title">Business Crowdfunding</h1>
<div class="hero-sub">Now anyone can fund your business.</div>

<form class="quote-panel">
  <p>Instant quote with a quick free application</p>
  <div class="field">First Name</div>
  <div class="field">Phone Number</div>
  <div class="field">E-mail Address</div>
  <div class="field">Select Your City</div>
  <span class="btn">Get Started</span>
</form>

<div class="rate-tab">CHECK YOUR RATE</div>
<div class="rate-panel">
  <div class="rate-row"><span>Business Loan Amount</span><span class="rate-input">€ 5000</span></div>
  <div class="slider"><i style="left:6%"></i><span class="lbl" style="left:0">€0</span><span class="lbl" style="right:0">€100,000</span></div>
  <div class="rate-row"><span>Monthly repayment</span><span class="rate-input">€ 22</span></div>
  <div class="slider"><i style="left:12%"></i><span class="lbl" style="left:0">€0</span><span class="lbl" style="right:0">€2,000</span></div>
  <div class="rate-summary">
    <span>Borrowing<b>€5,000</b></span>
    <span>Interest<b>€1,620</b></span>
    <span>Total to repay<b>€6,620</b></span>
  </div>
  <span class="btn">Check your rate</span>
</div>

<section class="about">
  <h2 class="section-title" style="margin-top:84px">What is Brook Ledger?</h2>
  <div class="divider"><span></span><i></i><span></span></div>
  <p class="lead">We are ready to offer you several types of loans.</p>
  <p class="intro">At Brook Ledger, we offer trustworthy small businesses a new viable alternative to borrowing from the banks. Real people like you can lend small amounts to great Irish businesses at very attractive interest rates. The Banks get bypassed, the wheels keep turning and everyone wins!</p>
  <div class="feature" style="left:210px;top:340px">
    <div class="diamond"><svg width="28" height="28" viewBox="0 0 28 28"><circle cx="14" cy="14" r="9" fill="none" stroke="#fff" stroke-width="3"/><path d="M14 8v12M10 11h6M10 17h6" stroke="#fff" stroke-width="2"/></svg></div>
    <h3>Borrowing</h3>
    <p>Businesses complete a detailed online application, which forms the basis of their business plan and will include background information on the business, detail on the purpose of the loan and business financials.</p>
  </div>
  <div class="feature" style="left:690px;top:340px">
    <div class="diamond"><svg width="28" height="28" viewBox="0 0 28 28"><path d="M4 20l7-7 5 5 8-9" fill="none" stroke="#fff" stroke-width="3"/></svg></div>
    <h3>Lending</h3>
    <p>This is a great opportunity for a lender to get a better return than leaving funds in a deposit account. Registering online as a lender takes 5 minutes. Once registered, lenders can browse the full detail on all loan applications and choose.</p>
  </div>
  <span class="btn">Learn more</span>
</section>

<section class="how" role="img" aria-label="Busy workshop interior, softly dimmed">
  <h2 class="section-title">How it works</h2>
  <p class="intro">Brook Ledger is the better way to get things done, and is as simple to use as 1-2-3.</p>
  <div class="step" style="left:100px">
    <div class="step-pic" role="img" aria-label="Owner signing up on a laptop"></div>
    <h4>SIGN UP FOR FREE</h4>
    <p>Create your account in minutes, then tell us about your business plans.</p>
  </div>
  <div class="step" style="left:330px">
    <div class="step-pic" role="img" aria-label="Business owner meeting lenders"></div>
    <h4>EASY BORROWING</h4>
    <p>Borrowers can choose to accept the loan before the auction ends.</p>
  </div>
  <div class="step" style="left:560px">
    <div class="step-pic" role="img" aria-label="New shop opening its doors"></div>
    <h4>START UP YOUR BUSINESS</h4>
    <p>Receive your funds quickly and put your growth plans into action.</p>
  </div>
  <div class="person" role="img" aria-label="Smiling businesswoman in a blazer"></div>
</section>

<section class="lend">
  <h2>Looking to Lend?</h2>
  <div class="sub">A smarter way to manage your money</div>
  <p class="intro">Lending on Brook Ledger is a great way to get better returns on your money, and you'll feel good knowing that you're helping small local businesses to get the economy back up and running!</p>
  <span class="btn">Start Lending Now</span>
  <div class="watch"><svg width="22" height="16" viewBox="0 0 22 16"><rect width="22" height="16" rx="4" fill="#fff"/><path d="M9 4l6 4-6 4z" fill="#f0531f"/></svg>or Watch How to Lend</div>
</section>

<section class="gigs">
  <h2 class="section-title">Check out our featured CrowdFunding gigs</h2>
  <p class="lead">Trusted by 100+ Irish Business Owners</p>
  <div class="video" style="left:22px;background:linear-gradient(135deg,#6c7a86,#3b4650)" role="img" aria-label="Video: café owner on his loan"><span class="play"><svg width="16" height="18"><path d="M2 1l13 8-13 8z" fill="#fff"/></svg></span></div>
  <div class="video" style="left:328px;background:linear-gradient(135deg,#8a7d72,#4c4038)" role="img" aria-label="Video: team in a workshop"><span class="play"><svg width="16" height="18"><path d="M2 1l13 8-13 8z" fill="#fff"/></svg></span></div>
  <div class="video" style="left:628px;background:linear-gradient(135deg,#4f7a4c,#2f4a3a)" role="img" aria-label="Video: farm business owner"><span class="play"><svg width="16" height="18"><path d="M2 1l13 8-13 8z" fill="#fff"/></svg></span></div>
  <div class="video" style="left:934px;background:linear-gradient(135deg,#7d3a34,#3e2422)" role="img" aria-label="Video: retailer in his shop"><span class="play"><svg width="16" height="18"><path d="M2 1l13 8-13 8z" fill="#fff"/></svg></span></div>
</section>

<section class="testimonials">
  <div class="quote-box">
    <div class="quote" style="left:40px"><span class="badge"></span><p>A unique and creative way to get a loan that boasts lower interest rates than most banks and credit card companies.</p></div>
    <div class="quote" style="left:590px"><span class="badge"></span><p>A unique and creative way to get a loan that boasts lower interest rates than most banks and credit card companies.</p></div>
    <span class="see-more">See what others are saying</span>
  </div>
</section>

<footer class="site-footer">
  <div class="footer-brand"><div class="brand-name">Brook Ledger</div><div class="brand-tag">the business lending people</div></div>
  <div class="social"><i></i><i></i><i></i><i></i></div>
  <div class="fcol" style="left:388px"><h5>Quick Links</h5><ul><li>The Marketplace</li><li>Lend</li><li>Borrow</li><li>About Us</li><li>CrowdFunding</li><li>Our Team</li><li>Press</li><li>Blog</li></ul></div>
  <div class="fcol" style="left:600px"><h5>Resources</h5><ul><li>FAQ</li><li>Guidelines</li><li>Contact Us</li></ul></div>
  <div class="fcol" style="left:800px"><h5>Legal</h5><ul><li>Terms of Service</li><li>Privacy Policy</li></ul></div>
  <div class="fcol" style="left:1000px"><h5>Seriously Secure</h5><ul><li>Privacy</li><li>Security</li><li>Confidentiality</li></ul><div class="seal"></div><div class="seal"></div></div>
  <div class="copyright">Copyright © Brook Ledger Ltd 2015, All rights reserved.</div>
</footer>

</body>
</html>
```